Landing Page for Bathroom Remodeling Webpage - Desktop and Mobile

I am looking for some help designing the "above the fold" area for my bathroom remodeling service page. Looking for something a little different than the rest. Typically remodeling companies just put a nice picture of a bathroom remodel but I would like to do something a little different / more creative. Below is a link to the current wireframe we are working on.
Current website is located at brellforgeplains.com
Again the biggest thing I am looking for is a design for the very top section but would love help on the rest of the page as well. You will see by viewing the link below the type of information we are looking to include on the page:
PLEASE DO INCLUDE WHAT THE MOBILE VERSION WOULD LOOK LIKE AS WELL.
Wireframe:
https://xd.quillvarn.com/view/3f8a1b2c-90de-4e7f-8a6b-1c2d3e4f5a6b-841c/
There are also comments in the link above you can read as well.
We like the idea of something interactive such as this...
https://pixelmoor.com/shots/5149273-Valdor-Scooter-Store-Animation
Attached is also the logo we want to use going forward
Target Market(s)
Residential homeowners, 30 years old+ with professional careers
Number of Pages Required
1 page
Look and feel

```html
<!DOCTYPE html>
<html lang="en">
<head>
<meta charset="utf-8">
<title>Brellforge – Bathroom Remodeling</title>
<link href="https://fonts.googleapis.com/css2?family=Poppins:wght@300;400;500;600;700&display=swap" rel="stylesheet">
<style>
  :root{
    --navy:#0f2a55;
    --red:#c8102e;
    --ink:#1c2a44;
    --white:#ffffff;
    --page:#ffffff;
    --hero-dark:#2b2d31;
    --hero-mid:#55585c;
    --rule:rgba(255,255,255,.55);
  }
  *{box-sizing:border-box;margin:0;padding:0}
  html,body{width:1200px;height:1200px;overflow:hidden;background:var(--page);font-family:'Poppins',sans-serif;color:var(--ink)}
  .canvas{position:relative;width:1200px;height:1200px}

  .desktop{position:absolute;left:43px;top:100px;width:773px;height:1008px;background:var(--white);box-shadow:0 1px 6px rgba(0,0,0,.22);overflow:hidden}
  .mobile{position:absolute;left:942px;top:100px;width:194px;height:471px;background:var(--white);box-shadow:0 1px 6px rgba(0,0,0,.22);overflow:hidden}

  .brand{position:absolute;display:flex;align-items:center;gap:5px;font-weight:700;color:var(--navy);letter-spacing:.2px}
  .brand-dot{border-radius:50%;background:var(--red);flex:none}

  .site-header{position:absolute;left:0;top:0;width:100%;height:49px;background:var(--white)}
  .site-header .brand{left:30px;top:0;height:49px;font-size:11.5px}
  .site-header .brand-dot{width:11px;height:11px}
  .main-nav a{position:absolute;top:0;line-height:49px;font-size:8.6px;font-weight:600;color:var(--navy);text-decoration:none}
  .main-nav a.is-active{color:var(--red)}
  .estimate-cta{position:absolute;right:0;top:0;width:107px;height:49px;background:var(--navy);color:var(--white);font-size:8.4px;font-weight:600;text-align:center;display:flex;flex-direction:column;justify-content:center;line-height:12px}

  .hero{position:absolute;left:0;top:49px;width:100%;height:435px;overflow:hidden}
  .hero-bg{position:absolute;inset:0;background:linear-gradient(100deg,#4a4d4f 0%,#5d605f 30%,#3e4044 60%,#2f3134 100%)}
  .hero-shade{position:absolute;inset:0;background:linear-gradient(180deg,rgba(0,0,0,.15) 0%,rgba(0,0,0,.05) 60%,rgba(20,18,18,.55) 100%)}
  .hero-title{position:absolute;left:49px;top:90px;color:var(--white);font-weight:700;font-size:44px;line-height:45px;letter-spacing:.3px}
  .hero-lead{position:absolute;left:51px;top:201px;color:var(--white);font-size:9.8px;line-height:14.5px;font-weight:400}
  .hero-lead b{font-weight:600}
  .feature-list{position:absolute;left:51px;top:267px;list-style:none;color:var(--white);font-size:9.8px;line-height:14.5px;font-weight:300}
  .feature-list li{display:flex;align-items:center;gap:9px}
  .tick{width:9px;height:8px;flex:none}

  .slide{position:absolute;border-radius:4px;overflow:hidden}
  .slide-a{background:linear-gradient(160deg,#6b5e52 0%,#3b3632 45%,#d9d4cc 70%,#1f1f20 100%)}
  .slide-b{background:linear-gradient(170deg,#8b8d90 0%,#a5a7a9 45%,#f1f1f1 75%,#9a9b9d 100%)}
  .slide-c{background:linear-gradient(175deg,#d9dadb 0%,#b9bcc0 55%,#7c8895 100%)}
  .hero .slide{top:53px;width:157px;height:284px}

  .slider-btn{position:absolute;border:1px solid var(--rule);border-radius:50%;display:flex;align-items:center;justify-content:center}
  .slider-rule{position:absolute;height:1px;background:rgba(255,255,255,.45)}
  .hero .slider-btn{width:30px;height:30px;top:351px}
  .hero .slider-rule{left:451px;right:0;top:366px}

  .schedule-band{position:absolute;left:0;top:484px;width:100%;height:60px;background:var(--navy);color:var(--white)}
  .schedule-band p{position:absolute;left:50px;top:0;line-height:60px;font-size:12.6px;font-weight:400}
  .schedule-btn{position:absolute;left:626px;top:16px;width:96px;height:27px;background:var(--white);border-radius:2px;color:var(--navy);font-size:9.2px;font-weight:600;display:flex;align-items:center;justify-content:center;gap:7px}

  .projects-title{position:absolute;left:0;width:100%;top:584px;text-align:center;font-size:21.5px;font-weight:300;color:var(--navy)}
  .projects-rule{position:absolute;left:362px;top:622px;width:48px;height:2px;background:var(--navy)}
  .project-card{position:absolute;top:667px;width:314px;height:211px;border-radius:5px;overflow:hidden}
  .project-card .photo{position:absolute;inset:0}
  .photo-kitchen{background:linear-gradient(180deg,#efefed 0%,#e3e3e1 45%,#8e8b86 75%,#4a3a2e 100%)}
  .photo-bath{background:linear-gradient(90deg,#2c2e30 0%,#3d3f41 28%,#cfd0d0 45%,#e9e9e8 70%,#d4d4d4 100%)}
  .project-caption{position:absolute;left:0;width:100%;top:164px;text-align:center;color:var(--white)}
  .project-caption h3{font-size:15px;font-weight:400;line-height:18px}
  .project-caption p{font-size:9.4px;font-weight:400;margin-top:3px}
  .learn-btn{position:absolute;left:347px;top:927px;width:78px;height:27px;border:1px solid var(--navy);border-radius:2px;color:var(--navy);font-size:9.2px;display:flex;align-items:center;justify-content:center}

  /* mobile */
  .m-header{position:absolute;left:0;top:0;width:100%;height:36px;background:var(--white)}
  .m-header .brand{left:12px;top:0;height:36px;font-size:10.5px}
  .m-header .brand-dot{width:10px;height:10px}
  .menu-icon{position:absolute;left:167px;top:13px}
  .m-hero{position:absolute;left:0;top:36px;width:100%;height:435px;overflow:hidden}
  .m-hero .hero-title{left:11px;top:36px;font-size:24.5px;line-height:31px}
  .m-hero .hero-lead{left:12px;top:111px;font-size:8.2px;line-height:14.4px}
  .m-hero .feature-list{left:12px;top:168px;font-size:9.6px;line-height:14.5px}
  .m-hero .feature-list li{gap:10px}
  .m-hero .slide{top:261px;width:71px;height:127px;border-radius:3px}
  .m-hero .slider-btn{width:14px;height:14px;top:397px}
  .m-hero .slider-rule{left:53px;right:0;top:404px}
</style>
</head>
<body>
<div class="canvas">

  <section class="desktop">
    <header class="site-header">
      <div class="brand"><span class="brand-dot"></span>BRELLFORGE</div>
      <nav class="main-nav">
        <a style="left:287px">Home</a>
        <a class="is-active" style="left:336px">Services</a>
        <a style="left:395px">Videos</a>
        <a style="left:449px">Gallery</a>
        <a style="left:503px">Blog</a>
        <a style="left:547px">About</a>
        <a style="left:597px">Contact</a>
      </nav>
      <div class="estimate-cta"><span>Get An Estimate</span><span>555-014-2287</span></div>
    </header>

    <div class="hero">
      <div class="hero-bg" role="img" aria-label="Softly lit modern bathroom with freestanding tub and large windows"></div>
      <div class="hero-shade"></div>
      <h1 class="hero-title">BATHROOM<br>REMODELING</h1>
      <p class="hero-lead">It's where you <b>start and end your day.</b><br>A bathroom remodel will make sure it<br><b>starts and ends right.</b></p>
      <ul class="feature-list">
        <li><svg class="tick" viewBox="0 0 10 8"><path d="M1 4.2 3.7 7 9 1" fill="none" stroke="#fff" stroke-width="1.8"/></svg>Our Process</li>
        <li><svg class="tick" viewBox="0 0 10 8"><path d="M1 4.2 3.7 7 9 1" fill="none" stroke="#fff" stroke-width="1.8"/></svg>3D Design</li>
        <li><svg class="tick" viewBox="0 0 10 8"><path d="M1 4.2 3.7 7 9 1" fill="none" stroke="#fff" stroke-width="1.8"/></svg>Material Packages</li>
        <li><svg class="tick" viewBox="0 0 10 8"><path d="M1 4.2 3.7 7 9 1" fill="none" stroke="#fff" stroke-width="1.8"/></svg>Helpful Articles</li>
        <li><svg class="tick" viewBox="0 0 10 8"><path d="M1 4.2 3.7 7 9 1" fill="none" stroke="#fff" stroke-width="1.8"/></svg>FAQ</li>
      </ul>
      <div class="slide slide-a" style="left:358px" role="img" aria-label="Dark marble bathroom with floating vanity and tall window"></div>
      <div class="slide slide-b" style="left:536px" role="img" aria-label="Grey stone shower wall with white freestanding tub"></div>
      <div class="slide slide-c" style="left:713px" role="img" aria-label="Bright bathroom vanity with chrome faucet"></div>
      <div class="slider-btn" style="left:358px"><svg width="8" height="10" viewBox="0 0 8 10"><path d="M5.5 1 2 5l3.5 4" fill="none" stroke="#fff" stroke-width="1.3"/></svg></div>
      <div class="slider-btn" style="left:401px"><svg width="8" height="10" viewBox="0 0 8 10"><path d="M2.5 1 6 5 2.5 9" fill="none" stroke="#fff" stroke-width="1.3"/></svg></div>
      <div class="slider-rule"></div>
    </div>

    <div class="schedule-band">
      <p>Schedule a free in home consultation via our online appointment scheduling system</p>
      <div class="schedule-btn"><svg width="10" height="10" viewBox="0 0 10 10"><rect x="0.5" y="1.5" width="9" height="8" fill="none" stroke="#0f2a55"/><rect x="0.5" y="1.5" width="9" height="2.2" fill="#0f2a55"/><path d="M2.5 5.5h1M4.5 5.5h1M6.5 5.5h1M2.5 7.5h1M4.5 7.5h1" stroke="#0f2a55"/></svg>Schedule</div>
    </div>

    <h2 class="projects-title">Get Inspired By Similar Projects</h2>
    <div class="projects-rule"></div>

    <article class="project-card" style="left:52px">
      <div class="photo photo-kitchen" role="img" aria-label="White kitchen with stainless appliances, pendant lights and bar stools"></div>
      <div class="project-caption"><h3>Lorem ipsum dolor sit amet</h3><p>Lorem ipsum dolor sit amet</p></div>
    </article>
    <article class="project-card" style="left:408px">
      <div class="photo photo-bath" role="img" aria-label="Bathroom with dark cabinetry, white counter and wall sconces"></div>
      <div class="project-caption"><h3>Lorem ipsum dolor sit amet</h3><p>Lorem ipsum dolor sit amet</p></div>
    </article>

    <div class="learn-btn">Learn More</div>
  </section>

  <section class="mobile">
    <header class="m-header">
      <div class="brand"><span class="brand-dot"></span>BRELLFORGE</div>
      <svg class="menu-icon" width="14" height="9" viewBox="0 0 14 9"><path d="M0 1h14M4 4.5h10M7 8h7" stroke="#0f2a55" stroke-width="1.6"/></svg>
    </header>
    <div class="m-hero">
      <div class="hero-bg" role="img" aria-label="Softly lit modern bathroom background"></div>
      <div class="hero-shade"></div>
      <h1 class="hero-title">BATHROOM<br>REMODELING</h1>
      <p class="hero-lead">It's where you <b>start and end your day.</b><br>A bathroom remodel will make sure it<br><b>starts and ends right.</b></p>
      <ul class="feature-list">
        <li><svg class="tick" viewBox="0 0 10 8"><path d="M1 4.2 3.7 7 9 1" fill="none" stroke="#fff" stroke-width="1.8"/></svg>Our Process</li>
        <li><svg class="tick" viewBox="0 0 10 8"><path d="M1 4.2 3.7 7 9 1" fill="none" stroke="#fff" stroke-width="1.8"/></svg>3D Design</li>
        <li><svg class="tick" viewBox="0 0 10 8"><path d="M1 4.2 3.7 7 9 1" fill="none" stroke="#fff" stroke-width="1.8"/></svg>Material Packages</li>
        <li><svg class="tick" viewBox="0 0 10 8"><path d="M1 4.2 3.7 7 9 1" fill="none" stroke="#fff" stroke-width="1.8"/></svg>Helpful Articles</li>
        <li><svg class="tick" viewBox="0 0 10 8"><path d="M1 4.2 3.7 7 9 1" fill="none" stroke="#fff" stroke-width="1.8"/></svg>FAQ</li>
      </ul>
      <div class="slide slide-a" style="left:12px" role="img" aria-label="Dark marble bathroom with floating vanity"></div>
      <div class="slide slide-b" style="left:93px" role="img" aria-label="Grey stone wall with white freestanding tub"></div>
      <div class="slide slide-c" style="left:174px" role="img" aria-label="Bright bathroom vanity"></div>
      <div class="slider-btn" style="left:12px"><svg width="5" height="6" viewBox="0 0 8 10"><path d="M5.5 1 2 5l3.5 4" fill="none" stroke="#fff" stroke-width="1.5"/></svg></div>
      <div class="slider-btn" style="left:32px"><svg width="5" height="6" viewBox="0 0 8 10"><path d="M2.5 1 6 5 2.5 9" fill="none" stroke="#fff" stroke-width="1.5"/></svg></div>
      <div class="slider-rule"></div>
    </div>
  </section>

</div>
</body>
</html>
```